Tobin Quartz Portal Page . It's guarantee project!

We need a clean and professional modern web application portal page
That includes the Login & Application Selection screen

Also, I need to design both Desktop and Mobile sizes.
We have an example design for our target

The application is Jetty Schedule and related data.
Our client is a bit conservative.

Theme color preferred : #00508B (main) #DF0D83 (secondary)

Target Market(s)

Oil & Fuel & Gasoline

Number of Pages Required

2 page

Font styles to use
Sans Serif

Colors
0054AA
0677BA
7BADD7
CADEEF
E8F1F8
E54698
E96AAD
F1A4CE
F9D9EA
FCEFF6

Requirements
Must have
• Login Page & Main Screen

```html
<!DOCTYPE html>
<html lang="en">
<head>
<meta charset="utf-8">
<title>Tobin Quartz Portal – Login &amp; Application Selection</title>
<link rel="stylesheet" href="https://fonts.googleapis.com/css2?family=Poppins:wght@300;400;500;600&display=swap">
<style>
:root{
  --canvas:#b4b4b4;
  --stage:#f5f5f5;
  --navy:#0d2c52;
  --navy-deep:#0a2446;
  --main:#00508B;
  --pink:#DF0D83;
  --ink:#1b2a4a;
  --white:#ffffff;
  --field-text:#8a8f99;
  --pill:rgba(128,156,196,.6);
}
*{box-sizing:border-box;margin:0;padding:0}
html,body{width:1200px;height:3386px;overflow:hidden}
body{position:relative;background:var(--canvas);font-family:"Poppins",sans-serif;color:var(--white)}
.section-label{position:absolute;left:76px;font-size:28px;font-weight:300;color:var(--white)}
.stage{position:absolute;left:0;top:2366px;width:1200px;height:1020px;background:var(--stage)}

.screen{position:absolute;overflow:hidden}
.screen-photo{position:absolute;inset:0;
  background:
   radial-gradient(ellipse at 30% 20%,rgba(40,90,120,.55),transparent 60%),
   radial-gradient(ellipse at 80% 70%,rgba(40,110,90,.35),transparent 55%),
   linear-gradient(160deg,#14365f 0%,var(--navy) 45%,var(--navy-deep) 100%)}

.brand{position:absolute;display:flex;align-items:center;gap:.35em;font-weight:600;color:var(--white);white-space:nowrap}
.brand-dot{width:1.1em;height:1.1em;border-radius:50%;background:var(--pink);flex:none}
.brand-header{left:21px;top:30px;font-size:11px}

.signin-card{position:absolute;border-radius:14px;
  background:linear-gradient(165deg,rgba(98,176,222,.95) 0%,rgba(104,150,200,.85) 60%,rgba(110,128,180,.8) 100%)}
.signin-title{position:absolute;font-weight:600}
.field{position:absolute;background:var(--white);color:var(--field-text);display:flex;align-items:center}
.btn-primary{position:absolute;background:var(--pink);color:var(--white);display:flex;align-items:center;justify-content:center}
.signup-note{position:absolute;left:0;right:0;text-align:center}
.signup-note a{color:var(--pink);text-decoration:underline}

.home-btn{position:absolute;border:1.5px solid rgba(255,255,255,.85);display:flex;align-items:center;justify-content:center;gap:6px;white-space:nowrap}
.home-btn svg{fill:var(--white)}
.user-pill{position:absolute;background:var(--pill);display:flex;align-items:center;justify-content:flex-end;white-space:nowrap}
.user-text{text-align:right;line-height:1.15}
.user-name{font-weight:500}
.avatar{border-radius:50%;background:var(--pink);overflow:hidden;flex:none}
.toggle{position:absolute;border:1.5px solid rgba(255,255,255,.85);border-radius:999px;display:flex;align-items:center;color:rgba(255,255,255,.8)}
.toggle-knob{border-radius:999px;background:#c9ced8}

.app-card{position:absolute;background:var(--white);color:var(--ink);font-weight:500}
.app-card svg{fill:none;stroke:var(--pink);stroke-width:2.4;stroke-linecap:round;stroke-linejoin:round}
.footer-note{position:absolute;left:0;right:0;text-align:center;color:var(--white)}
.footer-note a{color:var(--pink);text-decoration:underline}

.desk .app-card{top:170px;width:259px;height:250px;border-radius:30px;text-align:center;font-size:21px;line-height:1.2}
.desk .app-card svg{position:absolute;left:82px;top:58px;width:95px;height:95px}
.desk .app-card .label{position:absolute;left:0;right:0;top:190px}
.desk .app-card .label.two{top:168px}

.mob .app-card{left:38px;width:414px;height:155px;border-radius:18px;font-size:22px;line-height:1.15}
.mob .app-card svg{position:absolute;left:68px;top:36px;width:84px;height:84px}
.mob .app-card .label{position:absolute;left:175px;top:50%;transform:translateY(-50%)}

.scaled{position:absolute;transform-origin:0 0}
</style>
</head>
<body>

<svg width="0" height="0" style="position:absolute">
  <defs>
    <symbol id="ic-calendar" viewBox="0 0 100 100">
      <path d="M14 22 H86 L90 84 H10 Z"/><path d="M12 34 H88"/><path d="M10 84 L10 90 H90 L90 84"/>
      <path d="M30 14 V28 M50 14 V28 M70 14 V28"/>
      <path d="M32 42 V78 M46 42 V78 M60 42 V78 M74 42 V78 M20 52 H82 M19 64 H83"/>
      <path d="M50 70 l5 6 l10 -12"/>
    </symbol>
    <symbol id="ic-track" viewBox="0 0 100 100">
      <path d="M50 78 C36 62 30 54 30 44 a20 20 0 0 1 40 0 C70 54 64 62 50 78 Z"/>
      <circle cx="50" cy="44" r="8"/>
      <path d="M14 36 C26 22 74 22 86 36"/><path d="M6 40 l6 -3 M94 40 l-6 -3"/>
      <path d="M22 50 l-6 4 M78 50 l6 4 M26 60 l-5 5 M74 60 l5 5"/>
      <path d="M34 86 H66"/>
    </symbol>
    <symbol id="ic-perf" viewBox="0 0 100 100">
      <path d="M12 16 V56 M12 56 L28 40 L42 52 L60 36 L70 44 L88 22"/>
      <path d="M8 62 H92 M8 74 H92 M12 62 V84 M30 62 V84 M50 62 V84 M70 62 V84 M88 62 V84"/>
      <path d="M12 62 l-4 -4 M88 62 l4 -4"/>
    </symbol>
    <symbol id="ic-home" viewBox="0 0 20 20"><path d="M10 2 L19 10 H16 V18 H12 V13 H8 V18 H4 V10 H1 Z"/></symbol>
    <symbol id="ic-user" viewBox="0 0 40 40"><circle cx="20" cy="15" r="7" fill="#fff"/><path d="M7 36 C8 26 32 26 33 36 Z" fill="#fff"/></symbol>
  </defs>
</svg>

<div class="section-label" style="top:35px">Desktop</div>

<!-- Desktop login -->
<section class="screen desk" style="left:75px;top:101px;width:1050px;height:592px">
  <div class="screen-photo" role="img" aria-label="Aerial photo of a port terminal with stacked containers and cranes, dark blue tint"></div>
  <div class="brand" style="left:0;right:0;top:78px;justify-content:center;font-size:34px"><span class="brand-dot"></span>Tobin Quartz</div>
  <div class="signin-card" style="left:355px;top:189px;width:339px;height:225px">
    <div class="signin-title" style="left:24px;top:14px;font-size:22px">Sign In</div>
    <div class="field" style="left:25px;top:61px;width:293px;height:35px;border-radius:7px;padding-left:14px;font-size:11px">Email</div>
    <div class="field" style="left:25px;top:115px;width:293px;height:35px;border-radius:7px;padding-left:14px;font-size:11px">Password</div>
    <div class="btn-primary" style="left:25px;top:169px;width:293px;height:35px;border-radius:7px;font-size:13px">Sign In</div>
  </div>
  <div class="signup-note" style="top:430px;font-size:11px">Don’t have an account? <a>Sign Up</a> here</div>
</section>

<!-- Desktop home -->
<section class="screen desk" style="left:75px;top:723px;width:1050px;height:590px">
  <div class="screen-photo" role="img" aria-label="Aerial photo of a port terminal with stacked containers and cranes, dark blue tint"></div>
  <div class="brand brand-header"><span class="brand-dot"></span>Tobin Quartz</div>
  <div class="home-btn" style="left:132px;top:25px;width:81px;height:38px;border-radius:8px;font-size:12px"><svg width="13" height="13"><use href="#ic-home"/></svg>Home</div>
  <div class="user-pill" style="left:864px;top:24px;width:160px;height:38px;border-radius:6px;padding-right:10px;gap:6px">
    <div class="user-text"><div class="user-name" style="font-size:11px">Mara Velden</div><div style="font-size:7px">mara.velden@example.com</div></div>
    <div class="avatar" style="width:26px;height:26px"><svg width="26" height="26" viewBox="0 0 40 40"><use href="#ic-user"/></svg></div>
    <span style="font-size:10px">⌄</span>
  </div>
  <div class="toggle" style="left:970px;top:80px;width:46px;height:16px;padding:0 3px;gap:4px;font-size:7px"><span class="toggle-knob" style="width:17px;height:9px"></span>Off</div>
  <div class="app-card" style="left:75px"><svg><use href="#ic-calendar"/></svg><div class="label">Jetty Planning</div></div>
  <div class="app-card" style="left:386px"><svg><use href="#ic-track"/></svg><div class="label">Jetty Tracking</div></div>
  <div class="app-card" style="left:714px"><svg><use href="#ic-perf"/></svg><div class="label two">Jetty/Port<br>Performance</div></div>
  <div class="footer-note" style="top:552px;font-size:7px">Lorem ipsum dolor sit amet, consectetuer adipiscing elit, sed diam nonummy nibh euismod tincidunt ut laoreet dolore <a>magna aliquam</a> erat volutpat.</div>
</section>

<div class="section-label" style="top:1352px">Mobile</div>

<!-- Mobile login -->
<section class="screen" style="left:76px;top:1417px;width:489px;height:868px">
  <div class="screen-photo" role="img" aria-label="Aerial photo of a port terminal with stacked containers, dark blue tint"></div>
  <div class="brand" style="left:0;right:0;top:130px;justify-content:center;font-size:40px"><span class="brand-dot"></span>Tobin Quartz</div>
  <div class="signin-card" style="left:37px;top:299px;width:415px;height:293px;border-radius:20px">
    <div class="signin-title" style="left:27px;top:14px;font-size:30px">Sign In</div>
    <div class="field" style="left:23px;top:78px;width:368px;height:49px;border-radius:10px;padding-left:17px;font-size:15px">Email</div>
    <div class="field" style="left:23px;top:150px;width:368px;height:49px;border-radius:10px;padding-left:17px;font-size:15px">Password</div>
    <div class="btn-primary" style="left:23px;top:223px;width:368px;height:50px;border-radius:10px;font-size:18px">Sign In</div>
  </div>
  <div class="signup-note" style="top:614px;font-size:15px">Don’t have an account? <a>Sign Up</a> here</div>
</section>

<!-- Mobile home -->
<section class="screen mob" style="left:636px;top:1417px;width:489px;height:868px">
  <div class="screen-photo" role="img" aria-label="Aerial photo of a port terminal with stacked containers, dark blue tint"></div>
  <div class="brand" style="left:0;right:0;top:46px;justify-content:center;font-size:24px"><span class="brand-dot"></span>Tobin Quartz</div>
  <div class="home-btn" style="left:37px;top:116px;width:122px;height:59px;border-radius:10px;font-size:17px"><svg width="18" height="18"><use href="#ic-home"/></svg>Home</div>
  <div class="user-pill" style="left:220px;top:118px;width:237px;height:57px;border-radius:9px;padding-right:12px;gap:9px">
    <div class="user-text"><div class="user-name" style="font-size:16px">Mara Velden</div><div style="font-size:11px">mara.velden@example.com</div></div>
    <div class="avatar" style="width:42px;height:42px"><svg width="42" height="42" viewBox="0 0 40 40"><use href="#ic-user"/></svg></div>
    <span style="font-size:14px">⌄</span>
  </div>
  <div class="toggle" style="left:363px;top:201px;width:81px;height:29px;padding:0 5px;gap:8px;font-size:13px"><span class="toggle-knob" style="width:30px;height:15px"></span>Off</div>
  <div class="app-card" style="top:255px"><svg><use href="#ic-calendar"/></svg><div class="label">Jetty Planning</div></div>
  <div class="app-card" style="top:437px"><svg><use href="#ic-track"/></svg><div class="label">Jetty Tracking</div></div>
  <div class="app-card" style="top:622px"><svg><use href="#ic-perf"/></svg><div class="label">Jetty/Port<br>Performance</div></div>
  <div class="footer-note" style="top:812px;font-size:10px;padding:0 40px;line-height:1.2">Lorem ipsum dolor sit amet, consectetuer adipiscing elit, sed diam nonummy nibh euismod tincidunt ut laoreet dolore <a>magna aliquam</a> erat volutpat.</div>
</section>

<!-- Presentation area: flat screens -->
<div class="stage">
  <section class="screen desk scaled" style="left:236px;top:171px;width:1050px;height:590px;transform:scale(.74);border-radius:8px">
    <div class="screen-photo" role="img" aria-label="Aerial photo of a port terminal with stacked containers and cranes, dark blue tint"></div>
    <div class="brand brand-header"><span class="brand-dot"></span>Tobin Quartz</div>
    <div class="home-btn" style="left:132px;top:25px;width:81px;height:38px;border-radius:8px;font-size:12px"><svg width="13" height="13"><use href="#ic-home"/></svg>Home</div>
    <div class="user-pill" style="left:864px;top:24px;width:160px;height:38px;border-radius:6px;padding-right:10px;gap:6px">
      <div class="user-text"><div class="user-name" style="font-size:11px">Mara Velden</div><div style="font-size:7px">mara.velden@example.com</div></div>
      <div class="avatar" style="width:26px;height:26px"><svg width="26" height="26" viewBox="0 0 40 40"><use href="#ic-user"/></svg></div>
      <span style="font-size:10px">⌄</span>
    </div>
    <div class="toggle" style="left:970px;top:80px;width:46px;height:16px;padding:0 3px;gap:4px;font-size:7px"><span class="toggle-knob" style="width:17px;height:9px"></span>Off</div>
    <div class="app-card" style="left:75px"><svg><use href="#ic-calendar"/></svg><div class="label">Jetty Planning</div></div>
    <div class="app-card" style="left:386px"><svg><use href="#ic-track"/></svg><div class="label">Jetty Tracking</div></div>
    <div class="app-card" style="left:714px"><svg><use href="#ic-perf"/></svg><div class="label two">Jetty/Port<br>Performance</div></div>
    <div class="footer-note" style="top:552px;font-size:7px">Lorem ipsum dolor sit amet, consectetuer adipiscing elit, sed diam nonummy nibh euismod tincidunt ut laoreet dolore <a>magna aliquam</a> erat volutpat.</div>
  </section>

  <section class="screen mob scaled" style="left:852px;top:381px;width:489px;height:868px;transform:scale(.44);border-radius:30px">
    <div class="screen-photo" role="img" aria-label="Aerial photo of a port terminal with stacked containers, dark blue tint"></div>
    <div class="brand" style="left:0;right:0;top:46px;justify-content:center;font-size:24px"><span class="brand-dot"></span>Tobin Quartz</div>
    <div class="home-btn" style="left:37px;top:116px;width:122px;height:59px;border-radius:10px;font-size:17px"><svg width="18" height="18"><use href="#ic-home"/></svg>Home</div>
    <div class="user-pill" style="left:220px;top:118px;width:237px;height:57px;border-radius:9px;padding-right:12px;gap:9px">
      <div class="user-text"><div class="user-name" style="font-size:16px">Mara Velden</div><div style="font-size:11px">mara.velden@example.com</div></div>
      <div class="avatar" style="width:42px;height:42px"><svg width="42" height="42" viewBox="0 0 40 40"><use href="#ic-user"/></svg></div>
      <span style="font-size:14px">⌄</span>
    </div>
    <div class="toggle" style="left:363px;top:201px;width:81px;height:29px;padding:0 5px;gap:8px;font-size:13px"><span class="toggle-knob" style="width:30px;height:15px"></span>Off</div>
    <div class="app-card" style="top:255px"><svg><use href="#ic-calendar"/></svg><div class="label">Jetty Planning</div></div>
    <div class="app-card" style="top:437px"><svg><use href="#ic-track"/></svg><div class="label">Jetty Tracking</div></div>
    <div class="app-card" style="top:622px"><svg><use href="#ic-perf"/></svg><div class="label">Jetty/Port<br>Performance</div></div>
    <div class="footer-note" style="top:812px;font-size:10px;padding:0 40px;line-height:1.2">Lorem ipsum dolor sit amet, consectetuer adipiscing elit, sed diam nonummy nibh euismod tincidunt ut laoreet dolore <a>magna aliquam</a> erat volutpat.</div>
  </section>
</div>

</body>
</html>
```